K.L.T Services

We are needing business cards for a construction company that does everything from painting and detailing, maintenance, Sheetrock repairs, demolition, tile and wood floors. Also, K.L.T stands for Detailing, maintenance, and Painting. We would like the colors to be closer to the colors grey and light brown/khaki, but if there is any other suggestions that would go better with the design we are open to ideas.

Industry/Entity Type

Business

Contact Information for Business Card

Owner / Operator Owen Salcedo (555) 318-4927 / (555) 742- 0386

Font styles to use
Sans Serif

```html
<!DOCTYPE html>
<html lang="en">
<head>
<meta charset="UTF-8">
<title>K.L.T Services – Business Cards</title>
<link rel="stylesheet" href="https://fonts.googleapis.com/css2?family=Open+Sans:wght@400;600;700&display=swap">
<style>
  :root {
    --backdrop: #332e2b;
    --card-white: #ffffff;
    --gold: #c4a046;
    --ink: #2e2e2e;
  }
  * { margin: 0; padding: 0; box-sizing: border-box; }
  html, body {
    width: 1200px;
    height: 844px;
    overflow: hidden;
    background: var(--backdrop);
  }
  .sheet {
    position: relative;
    width: 1200px;
    height: 844px;
  }
  .card {
    position: absolute;
    top: 273px;
    width: 520px;
    height: 297px;
    border-radius: 3px;
    box-shadow: 0 12px 30px rgba(0,0,0,0.45);
  }
  .card--front { left: 50px; background: var(--card-white); }
  .card--back  { left: 630px; background: var(--gold); }

  .wordmark {
    font-family: "Open Sans", sans-serif;
    font-weight: 600;
    letter-spacing: 2px;
    line-height: 1;
  }

  .front-logo {
    position: absolute;
    top: 40px;
    right: 34px;
  }
  .front-logo .wordmark { font-size: 58px; color: var(--gold); }

  .contact {
    position: absolute;
    left: 34px;
    bottom: 30px;
    font-family: "Open Sans", sans-serif;
    color: var(--ink);
  }
  .contact__name { font-size: 17px; font-weight: 700; color: var(--gold); }
  .contact__role { font-size: 13px; margin-top: 2px; }
  .contact__phones { list-style: none; margin-top: 16px; font-size: 14px; }
  .contact__phones li { display: flex; align-items: center; gap: 7px; line-height: 20px; }
  .contact__phones svg { width: 11px; height: 11px; fill: var(--gold); }

  .back-logo {
    position: absolute;
    inset: 0;
    display: flex;
    align-items: center;
    justify-content: center;
    color: var(--card-white);
  }
  .back-logo .wordmark { font-size: 84px; }
</style>
</head>
<body>
<main class="sheet">
  <section class="card card--front" aria-label="Business card front">
    <div class="front-logo">
      <div class="wordmark">K.L.T</div>
    </div>
    <div class="contact">
      <p class="contact__name">Owen Salcedo</p>
      <p class="contact__role">Owner / Operator</p>
      <ul class="contact__phones">
        <li><svg viewBox="0 0 24 24" aria-hidden="true"><path d="M6.6 10.8a15.1 15.1 0 0 0 6.6 6.6l2.2-2.2a1 1 0 0 1 1-.25 11.4 11.4 0 0 0 3.6.57 1 1 0 0 1 1 1V20a1 1 0 0 1-1 1A17 17 0 0 1 3 4a1 1 0 0 1 1-1h3.5a1 1 0 0 1 1 1c0 1.25.2 2.450.57 3.57a1 1 0 0 1-.25 1z"/></svg>(555) 318-4927</li>
        <li><svg viewBox="0 0 24 24" aria-hidden="true"><path d="M6.6 10.8a15.1 15.1 0 0 0 6.6 6.6l2.2-2.2a1 1 0 0 1 1-.25 11.4 11.4 0 0 0 3.6.57 1 1 0 0 1 1 1V20a1 1 0 0 1-1 1A17 17 0 0 1 3 4a1 1 0 0 1 1-1h3.5a1 1 0 0 1 1 1c0 1.25.2 2.45.57 3.57a1 1 0 0 1-.25 1z"/></svg>(555) 742- 0386</li>
      </ul>
    </div>
  </section>

  <section class="card card--back" aria-label="Business card back">
    <div class="back-logo">
      <div class="wordmark">K.L.T</div>
    </div>
  </section>
</main>
</body>
</html>
```